Famous Australian Web Brand (Zentrivo.com.au) Needs a New Website & Logo

Zentrivo.com.au is one of the leading domain name registration businesses in Australia and is looking for an overhaul of its website and brand.

Zentrivo.com.au current products/services include domain name registration, web hosting, web site creation and SSL certificates.

In this design contest on Quorvane, we would like designers to create a new logo and new website design for Zentrivo.com.au.

Here is what contest entrants will need to create:
- 1 new logo
- 1 new home page design
- 1 internal page (pricing page)

The winning designer will receive the main prize of $750. In addition to this, the winning designer will have the opportunity to work with Zentrivo for the build of the full website and may get ongoing design work from Zentrivo.

thank you all for your designs, we are after a web 2.0 look and feel, please dont use serif fonts, lets use modern and sleek ones, i will upload some samples of one we like shortly

header is to be in black with some texturing, white fonts and the call to action buttons are in green.

for the 6 free services, please use round edges for the images with the text under it, as i will upload shortly and we would like custome images, not stockimage types please

im uploading a sample of a background image for the header, which is black with texturing and also and image for the footer/middle of the page which has the correct shading of the grey for the middle section

please see file 8 for the look we are trying to get with our site and for font ideas

Reason: we have decided to extend the contest for another 3 days as a couple of designers have requested a bit more time

Target Market(s)

People that might need to buy a domain name or start a website: small business owners; entrepreneurs; bloggers; everyone from mum-and-dad website owners to tech savvy entrepreneurs. Geographically we will be targeting Australia but this should not influence the design.

Industry/Entity Type

Build

Requirements
Must have
• The logo should:
- Have the text "Zentrivo"
- Be positioned in the top left hand corner of the website
- Be either a wordmark, pictorial or abstract logo. That is, text-only logos are acceptable but we are also interested in receiving logos with a mark to the left that could somehow represents the business that we’re in

The homepage should:
- Feel modern, slick, web2.0
- Have a horizontal menu with 4 menu items: About Us | Contact Us | My Cart | Login
- Include the logo at the top
- Include the content from this Word Document
- Include the rough layout and style from this JPG template layout

The interior page should:
- Have the same look and feel as the home page
- Include the rough layout and style from this JPG attachment
- Include the content from this second Word Document
Nice to have
• - Grey, white and black primary colors
- Buttons that are green or lime green with a web2.0 call to action
- Full-width design (i.e. across the screen like Quorvane)
Should not have
• - Do not include overt Australian references. While we are an Australian business we do not want Australian flags, kangaroos or Barnaby Wollop in our logo or on our website.
- Do not use the current red color scheme in the design. We want to move away from this.

```html
<!DOCTYPE html>
<html lang="en">
<head>
<meta charset="utf-8">
<title>Zentrivo – Domain Names</title>
<link href="https://fonts.googleapis.com/css2?family=Ubuntu:wght@300;400;500&family=Arimo:wght@400&display=swap" rel="stylesheet">
<style>
:root{
  --black:#000;
  --lime:#8fcc14;
  --lime-light:#b6e83a;
  --lime-dark:#6aa600;
  --page:#f3f5f3;
  --ink:#111;
  --white:#fff;
}
*{margin:0;padding:0;box-sizing:border-box}
html,body{width:918px;height:1200px;overflow:hidden}
body{position:relative;background:var(--page);font-family:"Ubuntu",sans-serif;color:var(--ink)}
.abs{position:absolute}

.site-header{left:0;top:0;width:918px;height:222px;background:var(--black)}
.header-panel{left:90px;top:0;width:738px;height:222px;background:linear-gradient(180deg,#2a2a2a 0%,#161616 45%,#0c0c0c 100%)}
.brand{left:108px;top:28px;display:flex;align-items:center;gap:10px}
.brand-dot{width:52px;height:52px;border-radius:50%;background:var(--lime)}
.brand-name{font-size:28px;font-weight:400;color:var(--white)}
.top-menu{right:118px;top:56px;font-size:12.5px;font-weight:300;color:var(--white);white-space:nowrap}
.top-menu span{margin:0 3px}
.tagline{left:171px;top:82px;font-size:25px;font-weight:300;line-height:27px;color:var(--white)}
.search-input{left:171px;top:148px;width:222px;height:28px;background:var(--white);border:1px solid #999}
.tld{left:402px;top:148px;width:75px;height:28px;background:var(--white);font-size:11px;padding:7px 8px;border:1px solid #999}
.tld svg{position:absolute;right:6px;top:3px}
.search-btn{left:487px;top:147px;width:32px;height:32px;border-radius:50%;background:radial-gradient(circle at 40% 30%,var(--lime-light),var(--lime-dark));border:2px solid #333}
.search-btn svg{position:absolute;left:6px;top:5px}
.sub-links{left:171px;top:191px;font-size:12.5px;font-weight:300;color:#ddd;display:flex;gap:20px;white-space:nowrap}
.call-cta{left:596px;top:118px;width:203px;height:74px;border-radius:8px;background:linear-gradient(180deg,var(--lime-light),var(--lime) 50%,var(--lime-dark));color:var(--white);font-size:18px;font-weight:500;line-height:25px;padding:12px 16px;white-space:nowrap}

.main-nav{left:0;top:222px;width:918px;height:32px;background:linear-gradient(180deg,var(--lime-light),var(--lime) 55%,var(--lime-dark))}
.main-nav a{position:absolute;top:8px;font-size:14px;color:var(--white);text-decoration:none}
.nav-sep{position:absolute;top:6px;width:2px;height:20px;background:var(--white)}

.video-card{top:277px;width:203px;height:83px;border-radius:7px;background:linear-gradient(180deg,var(--lime-light),var(--lime) 55%,var(--lime-dark))}
.video-thumb{position:absolute;left:9px;top:5px;width:92px;height:73px;border-radius:4px;background:linear-gradient(135deg,#d9c3b0,#8a5a3a)}
.play{position:absolute;left:15px;top:22px;width:30px;height:30px;border-radius:50%;background:#111}
.play svg{position:absolute;left:10px;top:8px}
.video-title{position:absolute;left:110px;top:19px;font-size:11px;line-height:15px;color:var(--white);white-space:nowrap}

.promo-bar{left:171px;top:383px;width:628px;height:74px;border-radius:8px;background:linear-gradient(180deg,#2a2a2a,#050505);color:var(--white);font-size:23px;font-weight:300;line-height:26px;padding:10px 28px;white-space:nowrap}
.promo-dot{position:absolute;right:12px;top:11px;width:52px;height:52px;border-radius:50%;background:var(--lime)}

.feature{width:203px}
.feature-img{width:203px;height:139px;border-radius:8px;background:radial-gradient(ellipse at 50% 45%,#8fcc14 0 28%,#3a3a3a 29%,#111 80%)}
.feature h3{font-size:17px;font-weight:400;margin-top:13px;white-space:nowrap}
.feature p{font-family:"Arimo",sans-serif;font-size:9.3px;line-height:12px;margin-top:5px;letter-spacing:-0.1px}

.site-footer{left:0;top:1062px;width:918px;height:138px;background:linear-gradient(180deg,#1c1c1c,#000)}
.foot-col{top:1078px;width:102px;color:var(--white)}
.foot-col h4{font-size:13px;font-weight:400;margin-bottom:8px;white-space:nowrap}
.foot-col ul{list-style:none}
.foot-col li{font-size:9.5px;padding:3px 0 5px;border-bottom:1px solid var(--white);white-space:nowrap}
.foot-contact{left:596px;top:1069px;width:203px;height:120px;border-radius:8px;background:#0a0a0a;color:var(--white);padding:12px 12px;white-space:nowrap}
.foot-contact .ask{font-size:13px}
.foot-contact .big{font-size:24px;letter-spacing:1px;line-height:32px;margin-top:2px}
</style>
</head>
<body>
<header class="abs site-header"></header>
<div class="abs header-panel"></div>
<div class="abs brand"><span class="brand-dot"></span><span class="brand-name">Zentrivo</span></div>
<nav class="abs top-menu">About Us<span>|</span>Contact Us<span>|</span>My Cart<span>|</span>Login</nav>
<h1 class="abs tagline">You get a lot more<br>than just a domain name.</h1>
<div class="abs search-input"></div>
<div class="abs tld">com.au<svg width="12" height="22" viewBox="0 0 12 22"><path d="M6 1L11 9H1Z" fill="#7bbf10"/><path d="M6 21L11 13H1Z" fill="#7bbf10"/></svg></div>
<div class="abs search-btn"><svg width="18" height="20" viewBox="0 0 18 20"><circle cx="10" cy="8" r="6" fill="none" stroke="#fff" stroke-width="2"/><path d="M6 12L2 17" stroke="#fff" stroke-width="2"/></svg></div>
<div class="abs sub-links"><span>Renew a domain</span><span>Transfer a domain</span><span>View Price List</span></div>
<div class="abs call-cta">HAVE A QUESTION?<br>CALL 1300 41 27 93</div>

<nav class="abs main-nav">
  <a style="left:170px">DOMAINS</a><span class="nav-sep" style="left:255px"></span>
  <a style="left:282px">CREATOR</a><span class="nav-sep" style="left:364px"></span>
  <a style="left:388px">EMAIL</a><span class="nav-sep" style="left:448px"></span>
  <a style="left:473px">HOSTING</a><span class="nav-sep" style="left:555px"></span>
  <a style="left:580px">MARKETING</a>
</nav>

<div class="abs video-card" style="left:171px"><div class="video-thumb" role="img" aria-label="Presenter video still"><span class="play"><svg width="12" height="14"><path d="M0 0L12 7L0 14Z" fill="#8fcc14"/></svg></span></div><div class="video-title">EVERYONE<br>NEEDS A<br>DOMAIN NAME</div></div>
<div class="abs video-card" style="left:383px"><div class="video-thumb" role="img" aria-label="Presenter video still"><span class="play"><svg width="12" height="14"><path d="M0 0L12 7L0 14Z" fill="#8fcc14"/></svg></span></div><div class="video-title">HOW YOU CAN<br>USE A DOMAIN<br>NAME</div></div>
<div class="abs video-card" style="left:596px"><div class="video-thumb" role="img" aria-label="Presenter video still"><span class="play"><svg width="12" height="14"><path d="M0 0L12 7L0 14Z" fill="#8fcc14"/></svg></span></div><div class="video-title">WHY CHOOSE<br>ZENTRIVO</div></div>

<div class="abs promo-bar">Everything your business needs to be successful<br>online is FREE with every domain name.<span class="promo-dot"></span></div>

<section class="abs feature" style="left:171px;top:480px"><div class="feature-img" role="img" aria-label="Laptop showing free 15 page website"></div><h3>Free 15 Page Website</h3><p>Create a professional, full-featured website in minutes without any technical knowledge. Choose from 4,000+ stunning website designs and customize your site with near-limitless options. Upload your own artwork for a truly personalised look.</p></section>
<section class="abs feature" style="left:383px;top:480px"><div class="feature-img" role="img" aria-label="Laptop showing professional email"></div><h3>Free Professional Email</h3><p>Having a personalised address that matches your domain name (for example, Tom@TomsPretzels.com or Sales@TomsPretzels.com) gives your company a much more professional image when you communicate with customers and associates.</p></section>
<section class="abs feature" style="left:596px;top:480px"><div class="feature-img" role="img" aria-label="Laptop showing website hosting"></div><h3>Free Website Hosting</h3><p>We provide the fast and secure hosting for your website. We take care of all the maintenance so all you have to do is create content for your site. Best of all, you don't have to pay a cent for hosting for as long as your domain is registered with us.</p></section>

<section class="abs feature" style="left:171px;top:757px"><div class="feature-img" role="img" aria-label="Laptop showing free 15 page website"></div><h3>Free 15 Page Website</h3><p>Create a professional, full-featured website in minutes without any technical knowledge. Choose from 4,000+ stunning website designs and customize your site with near-limitless options. Upload your own artwork for a truly personalised look.</p></section>
<section class="abs feature" style="left:383px;top:757px"><div class="feature-img" role="img" aria-label="Laptop showing professional email"></div><h3>Free Professional Email</h3><p>Having a personalised address that matches your domain name (for example, Tom@TomsPretzels.com or Sales@TomsPretzels.com) gives your company a much more professional image when you communicate with customers and associates.</p></section>
<section class="abs feature" style="left:596px;top:757px"><div class="feature-img" role="img" aria-label="Laptop showing website hosting"></div><h3>Free Website Hosting</h3><p>We provide the fast and secure hosting for your website. We take care of all the maintenance so all you have to do is create content for your site. Best of all, you don't have to pay a cent for hosting for as long as your domain is registered with us.</p></section>

<footer class="abs site-footer"></footer>
<div class="abs foot-col" style="left:171px"><h4>DOMAIN NAMES</h4><ul><li>REGISTER DOMAINS</li><li>TRANSFER DOMAINS</li><li>RENEW DOMAINS</li><li>NAME SERVERS</li></ul></div>
<div class="abs foot-col" style="left:311px"><h4>DOMAIN NAMES</h4><ul><li>REGISTER DOMAINS</li><li>TRANSFER DOMAINS</li><li>RENEW DOMAINS</li><li>NAME SERVERS</li></ul></div>
<div class="abs foot-col" style="left:456px"><h4>DOMAIN NAMES</h4><ul><li>REGISTER DOMAINS</li><li>TRANSFER DOMAINS</li><li>RENEW DOMAINS</li><li>NAME SERVERS</li></ul></div>
<div class="abs foot-contact"><div class="ask">HAVE A QUESTION FOR US?</div><div class="big">CONTACT US<br>1300 41 27 93</div></div>
</body>
</html>
```